Business Cards for Harborline Estates Partners, Inc.
Business Cards, Stationary, Etc.
Professional
Rocco Tamberlini
Broker
4710 SE Marigold Commons Lane
Suite 100
Boca Raton, Fl 33867
rocco@harborlinepfl.com
We prefer the use of icons, as opposed to wording for phone, fax, email.
I will need 2 options for each submission. The second option should allow for a picture to be inserted on the business card.
*Upon completion the winning designer will need to send a 2nd set of files, for another agent in the office. - Name, title, contact info to follow upon conclusion of Contest.

```html
<!DOCTYPE html>
<html lang="en">
<head>
<meta charset="utf-8">
<title>Harborline Estates Partners, Inc. — Business Card Options</title>
<link rel="stylesheet" href="https://fonts.googleapis.com/css2?family=Open+Sans:ital,wght@0,400;0,600;1,400&family=Exo+2:wght@400&display=swap">
<style>
  :root {
    --sheet: #ffffff;
    --navy: #3b4a66;
    --olive: #6f7c62;
    --ink: #3b4a66;
    --text: #555b66;
    --muted: #7b808a;
    --card: #ffffff;
  }
  * { box-sizing: border-box; margin: 0; padding: 0; }
  html, body { width: 1200px; height: 806px; overflow: hidden; background: var(--sheet); }
  body { position: relative; font-family: "Open Sans", Arial, sans-serif; color: var(--text); }

  .card {
    position: absolute; width: 528px; height: 331px;
    background: linear-gradient(90deg, var(--navy) 0 50%, var(--olive) 50% 100%);
    box-shadow: 0 1px 3px rgba(0,0,0,.25);
  }
  .card__face { position: absolute; inset: 12px; background: var(--card); }
  .card--a-front { left: 72px; top: 29px; }
  .card--b-front { left: 643px; top: 29px; }
  .card--a-back { left: 72px; top: 432px; }
  .card--b-back { left: 643px; top: 432px; }

  .caption {
    position: absolute; width: 528px; text-align: center;
    font-family: "Exo 2", Arial, sans-serif; font-variant: small-caps;
    font-size: 21px; letter-spacing: 3px; color: #444;
  }
  .caption--top-a { left: 72px; top: 396px; }
  .caption--top-b { left: 643px; top: 396px; }
  .caption--bot-a { left: 72px; top: 772px; }
  .caption--bot-b { left: 643px; top: 772px; }

  .brand { display: flex; align-items: center; gap: 10px; }
  .brand__mark { width: 22px; height: 22px; background: var(--olive); flex: none; }
  .brand__name { font-weight: 600; color: var(--ink); line-height: 1.05; }

  .card--a-front .brand { position: absolute; left: 0; right: 0; top: 52px; justify-content: center; }
  .card--a-front .brand__name { font-size: 24px; }
  .card--b-front .brand { position: absolute; left: 24px; top: 44px; }
  .card--b-front .brand__name { font-size: 20px; }

  .agent { font-size: 12px; font-style: italic; color: var(--text); }
  .agent__title { font-style: normal; font-size: 10px; margin-left: 4px; }
  .agent__bar { margin-left: 4px; color: var(--muted); font-style: normal; }
  .card--a-front .agent { position: absolute; left: 0; right: 0; top: 190px; text-align: center; }
  .card--b-front .agent { position: absolute; left: 24px; top: 200px; }

  .contact { position: absolute; font-size: 9px; color: var(--text); line-height: 16px; }
  .contact__row { display: flex; align-items: center; gap: 10px; white-space: nowrap; }
  .contact__item { display: inline-flex; align-items: center; gap: 4px; }
  .icon { width: 9px; height: 9px; fill: var(--navy); flex: none; }
  .card--a-front .contact { left: 0; right: 0; top: 242px; }
  .card--a-front .contact__row { justify-content: center; }
  .card--b-front .contact { left: 24px; top: 252px; }

  .photo-slot {
    position: absolute; right: 22px; top: 84px; width: 102px; height: 112px;
    border: 2px solid #cfd2d6; background: #fff;
    box-shadow: inset 0 0 0 4px #fff, inset 0 0 0 5px #e3e5e8;
  }

  .card__back-brand { position: absolute; inset: 0; display: flex; align-items: center; justify-content: center; }
  .card__back-brand .brand__mark { width: 40px; height: 40px; }
  .card__back-brand .brand__name { font-size: 26px; max-width: 300px; }
</style>
</head>
<body>

  <section class="card card--a-front" aria-label="Business card front, option A">
    <div class="card__face">
      <div class="brand"><span class="brand__mark"></span><span class="brand__name">Harborline Estates Partners, Inc.</span></div>
      <p class="agent">Rocco Tamberlini <span class="agent__bar">|</span><span class="agent__title">Broker</span></p>
      <div class="contact">
        <div class="contact__row">
          <span class="contact__item"><svg class="icon" viewBox="0 0 10 10"><path d="M5 0a3.5 3.5 0 0 0-3.5 3.5C1.5 6 5 10 5 10s3.5-4 3.5-6.5A3.5 3.5 0 0 0 5 0zm0 5a1.5 1.5 0 1 1 0-3 1.5 1.5 0 0 1 0 3z"/></svg>4710 SE Marigold Commons Lane Suite 100 Boca Raton, Fl 33867</span>
        </div>
        <div class="contact__row">
          <span class="contact__item"><svg class="icon" viewBox="0 0 10 10"><path d="M2 0l2 2.5-1 1.2a6 6 0 0 0 3.3 3.3l1.2-1L10 8l-1.5 2C4 9.6.4 6 0 1.5z"/></svg>954-555-0142</span>
          <span class="contact__item"><svg class="icon" viewBox="0 0 10 10"><path d="M2 0h6v3H2zM0 3.5h10V8H8v2H2V8H0zm3 3V9h4V6.5z"/></svg>561-555-0187</span>
          <span class="contact__item"><svg class="icon" viewBox="0 0 10 10"><path d="M0 2h10v6H0zm1 1v.3L5 6l4-2.7V3z"/></svg>rocco@harborlinepfl.com</span>
        </div>
      </div>
    </div>
  </section>

  <section class="card card--b-front" aria-label="Business card front, option B">
    <div class="card__face">
      <div class="brand"><span class="brand__mark"></span><span class="brand__name">Harborline Estates Partners, Inc.</span></div>
      <p class="agent">Rocco Tamberlini <span class="agent__bar">|</span><span class="agent__title">Broker</span></p>
      <div class="photo-slot" role="img" aria-label="Space for agent photograph"></div>
      <div class="contact">
        <div class="contact__row">
          <span class="contact__item"><svg class="icon" viewBox="0 0 10 10"><path d="M2 0l2 2.5-1 1.2a6 6 0 0 0 3.3 3.3l1.2-1L10 8l-1.5 2C4 9.6.4 6 0 1.5z"/></svg>954-555-0142</span>
          <span class="contact__item"><svg class="icon" viewBox="0 0 10 10"><path d="M2 0h6v3H2zM0 3.5h10V8H8v2H2V8H0zm3 3V9h4V6.5z"/></svg>561-555-0187</span>
          <span class="contact__item"><svg class="icon" viewBox="0 0 10 10"><path d="M0 2h10v6H0zm1 1v.3L5 6l4-2.7V3z"/></svg>rocco@harborlinepfl.com</span>
        </div>
        <div class="contact__row">
          <span class="contact__item"><svg class="icon" viewBox="0 0 10 10"><path d="M5 0a3.5 3.5 0 0 0-3.5 3.5C1.5 6 5 10 5 10s3.5-4 3.5-6.5A3.5 3.5 0 0 0 5 0zm0 5a1.5 1.5 0 1 1 0-3 1.5 1.5 0 0 1 0 3z"/></svg>4710 SE Marigold Commons Lane Suite 100 Boca Raton, Fl 33867</span>
        </div>
      </div>
    </div>
  </section>

  <p class="caption caption--top-a">Business Card Front Option A</p>
  <p class="caption caption--top-b">Business Card Front Option B</p>

  <section class="card card--a-back" aria-label="Business card reverse, option A">
    <div class="card__face">
      <div class="card__back-brand"><div class="brand"><span class="brand__mark"></span><span class="brand__name">Harborline Estates Partners, Inc.</span></div></div>
    </div>
  </section>

  <section class="card card--b-back" aria-label="Business card reverse, option B">
    <div class="card__face">
      <div class="card__back-brand"><div class="brand"><span class="brand__mark"></span><span class="brand__name">Harborline Estates Partners, Inc.</span></div></div>
    </div>
  </section>

  <p class="caption caption--bot-a">Business Card Front Option A</p>
  <p class="caption caption--bot-b">Business Card Front Option B</p>

</body>
</html>
```